Miel du Matin Immerse in the enchanting flavors of France at Miel du Matin

A menu that is French in style with the Eiffel Tower. A elegant menu that is in rich blue with red or gold trimmings, we are a French Bakey and Cafe

Target Market(s)

30 to 55 people

Industry/Entity Type

Restaurant

Font styles to use
Decorative

Colors
0054AA
0677BA
7BADD7
CADEEF
E8F1F8
EB3D1F
EC4F4E
F09395
F8D3D4
FCEDEE

Requirements
Must have
• the attachment "My Brunch Specials" is the Menu I want you to create, it has all the text, "My Brunch Special Complete" is a word version. The menu size should be 4 1/4 wide by 14 inches long 2 Sided. must have our logo at the top , Make the font larger, because our biggest complaint about our menu is it is hard to read
Nice to have
• I would love to incorporate the Eiffel Tower as a silhouette in the background
Should not have
• I do not want too many pictures or small print

```html
<!DOCTYPE html>
<html lang="en">
<head>
<meta charset="UTF-8">
<title>Miel du Matin — Brunch &amp; Drink Specials</title>
<link rel="stylesheet" href="https://fonts.googleapis.com/css2?family=Alegreya:wght@500&family=Alfa+Slab+One&family=Oswald:wght@300;500&family=Poppins:wght@500&display=swap">
<style>
:root{
  --navy:#15174f;
  --navy-ghost:rgba(44,50,132,.45);
  --red:#e0492a;
  --red-soft:rgba(224,73,42,.38);
  --white:#ffffff;
  --page:#ffffff;
}
*{margin:0;padding:0;box-sizing:border-box}
html,body{width:766px;height:1200px;overflow:hidden;background:var(--page)}
.canvas{position:relative;width:766px;height:1200px}
.panel{position:absolute;top:39px;width:358px;height:1111px;background:var(--navy);overflow:hidden;color:var(--white)}
.panel--brunch{left:20px}
.panel--drinks{left:388px}
.frame{position:absolute;inset:13px 14px;border:1px solid var(--red);border-radius:10px;pointer-events:none;z-index:3}
.tower-art{position:absolute;right:0;bottom:0;width:48px;height:540px;
  background:linear-gradient(180deg,rgba(224,73,42,0) 0%,var(--red-soft) 45%,rgba(224,73,42,.5) 100%);z-index:0}
.tower-ghost{position:absolute;left:0;right:0;bottom:0;height:560px;
  background:linear-gradient(180deg,rgba(44,50,132,0) 0%,var(--navy-ghost) 100%);z-index:0}
.brand{position:absolute;top:50px;left:0;right:0;text-align:center;z-index:2}
.brand-mark{display:block;width:34px;height:34px;margin:0 auto 16px;background:var(--red)}
.brand-name{font-family:"Oswald",sans-serif;font-weight:300;font-size:13px;letter-spacing:6px;color:var(--white)}
.section-title{position:absolute;left:0;right:0;text-align:center;font-family:"Alfa Slab One",serif;font-weight:400;color:var(--red);font-size:21px;line-height:26px;letter-spacing:3px;z-index:2}
.item{position:absolute;z-index:2}
.panel--brunch .item{left:40px;width:278px}
.panel--drinks .item{left:38px;width:290px}
.item-head{display:flex;justify-content:space-between;align-items:flex-end;padding-bottom:3px;border-bottom:1.5px dotted rgba(255,255,255,.7);margin-bottom:7px}
.item-name{font-family:"Alegreya",serif;font-weight:500;font-size:17.5px;line-height:1.05;color:var(--red)}
.item-price{font-family:"Oswald",sans-serif;font-weight:500;font-size:15px;line-height:1;color:var(--white);margin-right:18px}
.item-desc{font-family:"Poppins",sans-serif;font-weight:500;font-size:9.3px;line-height:11.3px;color:var(--white)}
</style>
</head>
<body>
<main class="canvas">

  <section class="panel panel--brunch">
    <div class="tower-art" role="img" aria-label="Eiffel Tower silhouette in red-orange at the lower right edge"></div>
    <div class="frame"></div>
    <header class="brand"><span class="brand-mark"></span><span class="brand-name">MIEL DU MATIN</span></header>
    <h1 class="section-title" style="top:132px">BRUNCH SPECIALS</h1>

    <article class="item" style="top:168px">
      <div class="item-head"><h2 class="item-name">Ratatouille &amp; eggs</h2><span class="item-price">$18</span></div>
      <p class="item-desc">Experience the essence of Provence with our Ratatouille, a vibrant medley of roasted squash, peppers, tomatoes, eggplant, infused with fragrant fresh herbs. Served with two perfectly poached eggs, and your choice of flavorful andouille sausage or crispy bacon. Accompanied by a side of crusty baguette. It's a hearty dish that celebrates the flavors of the Mediterranean countryside.</p>
    </article>

    <article class="item" style="top:297px">
      <div class="item-head"><h2 class="item-name">Le Grande Breakfast</h2><span class="item-price">$15</span></div>
      <p class="item-desc">Start your day in style with our Le Grande Breakfast, a feast fit for royalty. Customize your morning indulgence with two eggs cooked to your preference, paired with either savory bacon or succulent chicken sausage. Choose between a freshly baked baguette or a buttery croissant to accompany your meal. Complete your breakfast by selecting from an array of sides including crispy hash browns, savory roasted potatoes, or a refreshing fruit salad. Bon appetit!</p>
    </article>

    <article class="item" style="top:446px">
      <div class="item-head"><h2 class="item-name">Smoked Salmon Tartine</h2><span class="item-price">$15</span></div>
      <p class="item-desc">Delight in the luxurious flavors of our Smoked Salmon Tartine, a culinary masterpiece that elevates breakfast to new heights. Indulge in truffled scrambled eggs nestled atop smoked salmon, adorned with tangy pickled red onions, briny caper berries, crisp cucumber, juicy tomato, and peppery arugula. All artfully arranged on multigrain bread generously spread with herb-infused cream cheese.</p>
    </article>

    <article class="item" style="top:587px">
      <div class="item-head"><h2 class="item-name">Le Benedict Salmon</h2><span class="item-price">$15</span></div>
      <p class="item-desc">Savor the classic elegance of Eggs Benedict, featuring two perfectly poached eggs nestled on toasted English muffins, with luscious smoked salmon and ripe tomato slices crowned with a velvety lemon-infused Hollandaise sauce. A timeless brunch delight crafted to perfection.</p>
    </article>

    <article class="item" style="top:702px">
      <div class="item-head"><h2 class="item-name">Salmon Atlantique</h2><span class="item-price">$15</span></div>
      <p class="item-desc">Enjoy a bed of crisp mixed greens adorned with delicate smoked salmon, sweet golden raisins, creamy goat cheese, and crunchy walnuts. All dressed in a tantalizing balsamic vinaigrette that ties the elements together perfectly.</p>
    </article>

    <article class="item" style="top:809px">
      <div class="item-head"><h2 class="item-name">Beef Bourguignon</h2><span class="item-price">$15</span></div>
      <p class="item-desc">Indulge in our rich and comforting flavors of savory, tender beef slowly braised in red wine, creating a luscious sauce that envelops pearl onions, carrots, and mushrooms in a symphony of flavors. Served alongside buttered egg noodles. It's a hearty and soul-warming meal that promises pure culinary bliss.</p>
    </article>

    <article class="item" style="top:927px">
      <div class="item-head"><h2 class="item-name">Tourte au Poulet</h2><span class="item-price">$15</span></div>
      <p class="item-desc" style="width:255px">Discover the indulgent flavors of our Tourte au Poulet, a savory delight that marries tender marinated chicken with the richness of Swiss cheese and the sweetness of onions, all encased in layers of flaky pastry. Topped with a savory mushroom medley and decadent bechamel sauce. A true comfort classic to delight your senses.</p>
    </article>
  </section>

  <section class="panel panel--drinks">
    <div class="tower-ghost" role="img" aria-label="Faint Eiffel Tower silhouettes in the background"></div>
    <div class="frame"></div>
    <header class="brand"><span class="brand-mark"></span><span class="brand-name">MIEL DU MATIN</span></header>
    <h1 class="section-title" style="top:136px">DRINK SPECIALS</h1>

    <article class="item" style="top:170px">
      <div class="item-head"><h2 class="item-name">Bottomless Mimosa</h2><span class="item-price">$18</span></div>
      <p class="item-desc">Embark on an endless journey of delight with our Bottomless Mimosa, featuring Westbrook champagne, infusing each sip with a sparkling sensation. Tailor your experience with your preferred flavor profile - opt for the timeless twist of classic orange juice or tangy cranberry juice for a refreshing zing. Continuously poured to ensure your glass is always full.</p>
    </article>

    <article class="item" style="top:274px">
      <div class="item-head"><h2 class="item-name">Apple Cider-Mimosa</h2><span class="item-price">$15</span></div>
      <p class="item-desc">A delightful twist on the classic mimosa. Crafted with champagne and crisp apple cider. To elevate the experience, we adorn the glass with a caramel rim dipped in brown sugar, adding a touch of indulgent sweetness to every sip.</p>
    </article>

    <article class="item" style="top:362px">
      <div class="item-head"><h2 class="item-name">Blood Orange or<br>Pineapple Spritz</h2><span class="item-price" style="align-self:center">$15</span></div>
      <p class="item-desc">Introducing our vibrant spritz cocktail, a tantalizing blend of Harlow &amp; Finch's premium Velka Vodka, sweet vermouth, and a touch of sweetness from a carefully muddled sugar cube. This effervescent libation reaches new heights with the addition of bubbly Fontclair, your choice of either Blood Orange or Pineapple syrup injects a burst of fruity allure into every sip.</p>
    </article>

    <article class="item" style="top:493px">
      <div class="item-head"><h2 class="item-name">Peach Bellini</h2><span class="item-price">$15</span></div>
      <p class="item-desc">Try our perfectly balanced Peach Bellini with each sip you capture the crispness of champagne with the irresistible sweetness of peach. It's a sublime fusion</p>
    </article>

    <article class="item" style="top:562px">
      <div class="item-head"><h2 class="item-name">Espresso Martini</h2><span class="item-price">$15</span></div>
      <p class="item-desc">Our Espresso Martini is a decadent blend of bold espresso, rich chocolate martini, and luxurious Bellacourt chocolate syrup. It's the ultimate indulgence for coffee and chocolate lovers alike.</p>
    </article>

    <article class="item" style="top:647px">
      <div class="item-head"><h2 class="item-name">Kir Royale</h2><span class="item-price">$15</span></div>
      <p class="item-desc">Our Kir Royale is a delightful fusion of the crisp, sparkling champagne bubbles and the sweet sophistication of black currant. a luxurious and ndulgent drink that's perfect for any occasion.</p>
    </article>

    <h1 class="section-title" style="top:731px">LATTE</h1>

    <article class="item" style="top:761px">
      <div class="item-head"><h2 class="item-name">Truffle Latte</h2><span class="item-price">$15</span></div>
      <p class="item-desc">We start with rich Bellacourt chocolate, known for its velvety smoothness and intense flavor. Then, we add a drizzle of salted caramel, adding a perfect balance of sweetness and a hint of savory richness. Finally, we combine this delightful blend with perfectly steamed milk to create a creamy and indulgent latte that will satisfy even</p>
    </article>

    <article class="item" style="top:868px">
      <div class="item-head"><h2 class="item-name">Napoleon Latte</h2><span class="item-price">$15</span></div>
      <p class="item-desc">We start with our rich espresso, renowned for its bold and robust character. Then, we add a luscious combination of hazelnut and vanilla syrup, creating a symphony of sweetness and nutty richness. As the final touch, we crown this masterpiece with the velvety smoothness of perfectly steamed milk.</p>
    </article>

    <article class="item" style="top:976px">
      <div class="item-head"><h2 class="item-name">Chai Latte</h2><span class="item-price">$15</span></div>
      <p class="item-desc">Our robust chai tea concentrate, infused with a symphony of cinnamon, cardamom, cloves, and ginger, sets the stage for a journey of aromatic delight. Paired with velvety steamed milk, each sip offers a harmonious blend of bold spices and creamy richness. Topped with a sprinkle of cinnamon, it's</p>
    </article>
  </section>

</main>
</body>
</html>
```